Business Card for Mortuary

We need a business card design for our mortuary. We are not the "traditional" mortuary and specialize in simple cremations and burials. We use a two sided card.

Industry/Entity Type

Funeral Home

Contact Information for Business Card

One side we would like to have with the general information of the mortuary:
Address: 4127 E. Larkspur Ave, Sun City, AZ 85399
Phone: 623-555-0142
email: hello@willowbendmortuary.example
website: willowbendmortuary.example

On the other side would like to have the information of employee:
Name: Mark T. Ellis
Email: mark@willowbendmortuary.example
Title: Funeral Director
Text: 602-555-0187

Font styles to use
Serif
Sans Serif

Requirements
Should not have
• Do not put any gothic images or things like a hearse or tombstone.

```html
<!DOCTYPE html>
<html lang="en">
<head>
<meta charset="utf-8">
<title>Willowbend Mortuary – Business Card</title>
<link href="https://fonts.googleapis.com/css2?family=Roboto:wght@400;500;700&display=swap" rel="stylesheet">
<style>
  :root {
    --page: #e4e4e2;
    --card-white: #ffffff;
    --card-black: #000000;
    --green: #86bd3f;
    --green-dark: #5c9e32;
    --ink: #111111;
    --text-grey: #555555;
    --rule: #6a6a6a;
  }
  * { box-sizing: border-box; margin: 0; padding: 0; }
  html, body { width: 1200px; height: 1200px; overflow: hidden; }
  body {
    background: var(--page);
    font-family: "Roboto", Arial, sans-serif;
    position: relative;
  }
  .card {
    position: absolute;
    left: 200px;
    width: 800px;
    height: 456px;
    border-radius: 26px;
    overflow: hidden;
  }
  .card--front { top: 150px; background: var(--card-white); }
  .card--back { top: 660px; background: var(--card-black); }

  .brand {
    position: absolute;
    display: flex;
    align-items: center;
  }
  .brand__mark { border-radius: 50%; background: var(--green); flex: none; }
  .brand__name {
    font-weight: 700;
    text-transform: uppercase;
    line-height: 0.9;
  }
  .brand__tagline {
    border-left: 1px solid var(--green);
    line-height: 1.15;
  }

  .card--front .brand { right: 40px; top: 92px; gap: 10px; }
  .card--front .brand__mark { width: 30px; height: 30px; }
  .card--front .brand__name { font-size: 34px; color: var(--ink); }
  .card--front .brand__tagline { font-size: 17px; color: var(--green); padding-left: 5px; }

  .person { position: absolute; left: 42px; top: 193px; }
  .person__name { font-size: 27px; font-weight: 700; color: var(--green); }
  .person__title { font-size: 18px; font-weight: 500; color: var(--ink); margin-top: 2px; }

  .divider {
    position: absolute; left: 42px; right: 45px; top: 263px;
    border-top: 1px solid var(--rule);
  }

  .contacts {
    position: absolute; left: 42px; top: 286px;
    list-style: none; font-size: 18px; color: var(--text-grey);
  }
  .contacts li { display: flex; align-items: center; gap: 8px; height: 23px; }
  .contacts svg { width: 16px; height: 16px; fill: var(--green); flex: none; }

  .address {
    position: absolute; right: 45px; top: 308px;
    text-align: right; font-size: 18px; line-height: 23px; color: var(--text-grey);
    font-style: normal;
  }

  .wave { position: absolute; left: 0; bottom: 0; width: 800px; height: 64px; display: block; }

  .card--back .brand { left: 50%; top: 50%; transform: translate(-50%, -50%); gap: 14px; }
  .card--back .brand__mark { width: 44px; height: 44px; }
  .card--back .brand__name { font-size: 48px; color: #ffffff; }
  .card--back .brand__tagline {
    font-size: 27px; color: #ffffff; padding-left: 7px; border-left-color: #ffffff;
  }
</style>
</head>
<body>

<section class="card card--front" aria-label="Employee side">
  <div class="brand">
    <span class="brand__mark"></span>
    <div class="brand__name">Willowbend<br>Mortuary</div>
    <div class="brand__tagline">Affordable<br>Cremation<br>and Burial</div>
  </div>

  <div class="person">
    <h1 class="person__name">Mark T. Ellis</h1>
    <p class="person__title">Funeral Director</p>
  </div>

  <div class="divider"></div>

  <ul class="contacts">
    <li>
      <svg viewBox="0 0 16 16" aria-hidden="true"><path d="M3.6 1.2l2.2 2.6-1.2 1.8c.9 2 2.6 3.7 4.6 4.6l1.8-1.2 2.6 2.2-1.3 2.4C7.6 13.4 2.6 8.4 1.2 3.7z"/></svg>
      602-555-0187
    </li>
    <li>
      <svg viewBox="0 0 16 16" aria-hidden="true"><path d="M8 1a7 7 0 0 0-6 10.6L1 15l3.5-1A7 7 0 1 0 8 1zm0 1.6a5.4 5.4 0 1 1-2.9 10l-.3-.2-1.5.4.4-1.4-.2-.3A5.4 5.4 0 0 1 8 2.6z"/></svg>
      623-555-0142
    </li>
    <li>
      <svg viewBox="0 0 16 16" aria-hidden="true"><path d="M2 4h12v1.2L8 9 2 5.2zm0 2.6l6 3.8 6-3.8V12H2z"/></svg>
      mark@willowbendmortuary.example
    </li>
    <li>
      <svg viewBox="0 0 16 16" aria-hidden="true"><path d="M2 4h12v1.2L8 9 2 5.2zm0 2.6l6 3.8 6-3.8V12H2z"/></svg>
      hello@willowbendmortuary.example
    </li>
  </ul>

  <address class="address">
    4127 E. Larkspur Ave<br>
    Sun City, AZ 85399<br>
    www.willowbendmortuary.example
  </address>

  <svg class="wave" viewBox="0 0 800 64" preserveAspectRatio="none" aria-hidden="true">
    <path d="M0 10 C180 26 330 32 520 12 C610 3 700 4 800 34 L800 64 L0 64 Z" fill="var(--green-dark)"/>
    <path d="M0 28 C200 44 360 36 520 20 C620 10 700 8 800 36 L800 64 L0 64 Z" fill="#ffffff"/>
    <path d="M0 31 C200 47 360 39 520 23 C620 13 700 11 800 38 L800 64 L0 64 Z" fill="var(--green)"/>
  </svg>
</section>

<section class="card card--back" aria-label="Company side">
  <div class="brand">
    <span class="brand__mark"></span>
    <div class="brand__name">Willowbend<br>Mortuary</div>
    <div class="brand__tagline">Affordable<br>Cremation<br>and Burial</div>
  </div>
</section>

</body>
</html>
```